High end boutique food product label

We are looking for a label design to be used on our range of high end food products. We don't have a design or colour scheme in mind and are interested to see what ideas are submitted.
We would like it to feel sophisticated, chic, and eye-catching.
All of our products are handmade in Australia using Australian ingredients.
The graphics for the label will need to be scaleable to be fit a variety of labels from small squat jars with labels sized 3.5cm high and 7cm wide, to tall thin bottles with labels that are 14cm high and 4.5cm wide.
We would be interested in working with the winning designer to create these different sized labels.
The label submitted for this project should be 14cm high and 4.5cm wide, it should include our logo (file supplied in .jpeg and .ai), the product name 'Extra Virgin Olive Oil' and the size '250ml'.
This is just the front label on a bottle, we are not expecting a rear label to be created currently.
You are welcome to use any fonts you think will look good but the fonts used in our logo are Allaina Medium and Bebas Kai Regular.

```html
<!DOCTYPE html>
<html lang="en">
<head>
<meta charset="utf-8">
<title>Kestrel Pantry — Label Range</title>
<link href="https://fonts.googleapis.com/css2?family=Abril+Fatface&family=Barlow:wght@400;500&display=swap" rel="stylesheet">
<style>
  :root {
    --paper: #f5f3ee;
    --label-black: #1a1a1a;
    --label-deep: #141414;
    --ink-light: #ecebe6;
    --gold: #c8a24a;
    --almond: #b27a46;
    --olive: #a8a848;
    --leaf: #6d8a4e;
    --tomato: #b8261f;
  }
  * { margin: 0; padding: 0; box-sizing: border-box; }
  html, body { width: 1200px; height: 979px; overflow: hidden; background: var(--paper); }
  .canvas { position: relative; width: 1200px; height: 979px; background: var(--paper); }
  .label { position: absolute; color: var(--ink-light); font-family: "Barlow", sans-serif; }
  .label--pouch { left: 133px; top: 262px; width: 397px; height: 645px; background: var(--label-black); }
  .label--bottle { left: 597px; top: 366px; width: 144px; height: 466px; background: var(--label-deep); }
  .label--jar { left: 789px; top: 612px; width: 283px; height: 237px; background: var(--label-black); }
  .brand { position: absolute; transform: translateX(-50%); text-align: center; font-family: "Barlow", sans-serif; font-weight: 500; color: var(--ink-light); line-height: 1.05; white-space: nowrap; }
  .eyebrow, .tagline, .size { position: absolute; font-weight: 400; white-space: nowrap; }
  .title { position: absolute; font-family: "Abril Fatface", serif; font-weight: 400; line-height: 0.95; white-space: nowrap; }
  .rule { position: absolute; height: 3px; background: var(--gold); }
  .food { position: absolute; border-radius: 50%; }
  .food--almond { background: var(--almond); }
  .food--olive { background: var(--olive); }
  .food--leaf { background: var(--leaf); border-radius: 50% 0; }
  .food--tomato { background: var(--tomato); }
</style>
</head>
<body>
<main class="canvas">

  <section class="label label--pouch">
    <div class="brand" style="left:194px; top:168px; font-size:26px;">Kestrel<br>Pantry</div>
    <p class="eyebrow" style="left:56px; top:278px; font-size:17px;">Roasted &amp; Salted</p>
    <h2 class="title" style="left:55px; top:300px; font-size:46px;">Almonds</h2>
    <span class="rule" style="left:52px; top:358px; width:50px;"></span>
    <p class="tagline" style="left:52px; top:368px; font-size:13px;">Handmade in Australia</p>
    <p class="size" style="left:62px; top:500px; font-size:12px;">NET WT 7 OZ (196g)</p>
    <div class="food food--almond" role="img" aria-label="Almond" style="left:57px; top:192px; width:42px; height:68px;"></div>
    <div class="food food--almond" role="img" aria-label="Almond" style="left:297px; top:162px; width:44px; height:68px; transform:rotate(30deg);"></div>
    <div class="food food--almond" role="img" aria-label="Almond" style="left:285px; top:382px; width:42px; height:70px; transform:rotate(-15deg);"></div>
    <div class="food food--almond" role="img" aria-label="Almond" style="left:100px; top:418px; width:40px; height:62px; transform:rotate(60deg);"></div>
    <div class="food food--almond" role="img" aria-label="Almond" style="left:203px; top:508px; width:40px; height:68px; transform:rotate(15deg);"></div>
  </section>

  <section class="label label--bottle">
    <div class="brand" style="left:72px; top:86px; font-size:19px;">Kestrel<br>Pantry</div>
    <p class="eyebrow" style="left:17px; top:189px; font-size:12px;">Extra Virgin</p>
    <h2 class="title" style="left:15px; top:206px; font-size:33px;">Olive<br>Oil</h2>
    <span class="rule" style="left:18px; top:276px; width:38px; height:2px;"></span>
    <p class="tagline" style="left:17px; top:284px; font-size:10px;">Handmade in Australia</p>
    <p class="size" style="left:16px; top:425px; font-size:11px;">250ml</p>
    <div class="food food--olive" role="img" aria-label="Green olive" style="left:101px; top:17px; width:32px; height:24px; transform:rotate(-20deg);"></div>
    <div class="food food--leaf" role="img" aria-label="Olive leaf" style="left:20px; top:26px; width:30px; height:12px; transform:rotate(-45deg);"></div>
    <div class="food food--leaf" role="img" aria-label="Olive leaf" style="left:72px; top:160px; width:50px; height:12px; transform:rotate(40deg);"></div>
    <div class="food food--olive" role="img" aria-label="Green olive" style="left:16px; top:310px; width:36px; height:28px; transform:rotate(-25deg);"></div>
    <div class="food food--leaf" role="img" aria-label="Olive leaf" style="left:85px; top:325px; width:44px; height:12px; transform:rotate(-45deg);"></div>
    <div class="food food--leaf" role="img" aria-label="Olive leaf" style="left:15px; top:370px; width:46px; height:12px; transform:rotate(35deg);"></div>
    <div class="food food--olive" role="img" aria-label="Green olive" style="left:88px; top:414px; width:42px; height:32px; transform:rotate(20deg);"></div>
  </section>

  <section class="label label--jar">
    <div class="brand" style="left:141px; top:40px; font-size:19px;">Kestrel<br>Pantry</div>
    <p class="eyebrow" style="left:21px; top:93px; font-size:12px;">With Herbs</p>
    <h2 class="title" style="left:21px; top:109px; font-size:31px;">Sun-Dried<br>Tomatoes</h2>
    <span class="rule" style="left:22px; top:183px; width:30px; height:2px;"></span>
    <p class="tagline" style="left:21px; top:190px; font-size:9px;">Handmade in Australia</p>
    <p class="size" style="left:21px; top:214px; font-size:10px;">NET WT. 8.5 OZ (241g)</p>
    <div class="food food--tomato" role="img" aria-label="Sun-dried tomato" style="left:28px; top:6px; width:40px; height:68px; transform:rotate(10deg);"></div>
    <div class="food food--tomato" role="img" aria-label="Sun-dried tomato" style="left:212px; top:60px; width:64px; height:62px;"></div>
    <div class="food food--tomato" role="img" aria-label="Sun-dried tomato" style="left:175px; top:175px; width:72px; height:60px; transform:rotate(30deg);"></div>
  </section>

</main>
</body>
</html>
```